Corinne Dabney Interiors business cards

We need a DOUBLE SIDED business card design that is simple, elegant and modern. We are a rapidly growing Interior Design Firm, and our brand colours are blush pink, navy, and antique gold, so we require some or all of these colours to be used. The final design should portray elegance, simplicity, and have a modern feel. We have upload inspiration photos that have the feel we're looking for.

Industry/Entity Type

Interior Design

Contact Information for Business Card

Contact information and LOGO

Colors
EB3D1F
EC4F4E
F09395
F8D3D4
FCEDEE

Requirements
Must have
• Navy, the right shade of blush pink, and antique gold

```html
<!DOCTYPE html>
<html lang="en">
<head>
<meta charset="utf-8">
<title>Corinne Dabney Interiors — Business Cards</title>
<link rel="stylesheet" href="https://fonts.googleapis.com/css2?family=Jost:wght@400;500&family=Arimo:wght@400;700&display=swap">
<style>
  :root {
    --navy: #283673;
    --navy-deep: #1b2560;
    --blush: #f0bcb3;
    --blush-light: #f8d3d4;
    --blush-soft: #fcedee;
    --gold: #8c6d1f;
    --ink: #55575c;
    --paper: #ffffff;
    --backdrop: #e9e9eb;
  }
  * { box-sizing: border-box; margin: 0; padding: 0; }
  html, body { width: 1200px; height: 802px; overflow: hidden; }
  body {
    background: var(--backdrop);
    display: flex;
    align-items: center;
    justify-content: center;
    gap: 40px;
    font-family: "Arimo", Arial, sans-serif;
  }
  .card {
    position: relative;
    width: 540px;
    height: 309px;
    background: var(--paper);
    overflow: hidden;
    box-shadow: 0 10px 30px rgba(0,0,0,.12);
  }
  .card-art { position: absolute; inset: 0; width: 100%; height: 100%; }
  .brand-mark {
    position: absolute;
    display: flex;
    align-items: center;
    gap: 10px;
    font-family: "Jost", sans-serif;
    font-weight: 500;
    color: var(--gold);
    text-transform: uppercase;
    letter-spacing: .04em;
  }
  .brand-mark .brand-square { background: var(--navy); flex: none; }
  /* front */
  .card--front .brand-mark { left: 34px; top: 70px; font-size: 13px; }
  .card--front .brand-square { width: 14px; height: 14px; }
  .holder { position: absolute; left: 34px; top: 150px; }
  .holder-name { font-weight: 700; font-size: 20px; color: var(--gold); }
  .holder-title { font-size: 13px; color: var(--ink); margin-top: 2px; }
  .contacts { position: absolute; left: 34px; top: 208px; list-style: none; }
  .contacts li {
    display: flex; align-items: center; gap: 8px;
    font-size: 13px; color: var(--ink); line-height: 22px;
  }
  .contacts svg { width: 12px; height: 12px; flex: none; }
  .address {
    position: absolute; left: 300px; top: 150px;
    font-size: 13px; line-height: 19px; color: var(--ink);
  }
  .edge-tab { position: absolute; left: 0; top: 212px; width: 5px; height: 24px; background: var(--gold); }
  /* back */
  .card--back .brand-mark { left: 40px; top: 190px; font-size: 20px; }
  .card--back .brand-square { width: 20px; height: 20px; }
</style>
</head>
<body>

<section class="card card--front" aria-label="Business card front">
  <svg class="card-art" viewBox="0 0 540 309" aria-hidden="false">
    <defs>
      <linearGradient id="blushFront" x1="0" y1="0" x2="1" y2="1">
        <stop offset="0" stop-color="#f8d3d4"/>
        <stop offset="1" stop-color="#eeb2a6"/>
      </linearGradient>
    </defs>
    <polygon points="200,0 540,0 540,62 150,70" fill="url(#blushFront)" role="img" aria-label="Blush marble texture band"/>
    <polygon points="395,0 540,0 540,309 480,309" fill="var(--navy)" role="img" aria-label="Navy textured panel"/>
    <line x1="150" y1="70" x2="540" y2="60" stroke="var(--gold)" stroke-width="2"/>
  </svg>

  <div class="brand-mark"><span class="brand-square"></span>Corinne Dabney Interiors</div>

  <div class="holder">
    <p class="holder-name">Marcus Ellery</p>
    <p class="holder-title">Manager</p>
  </div>

  <ul class="contacts">
    <li>
      <svg viewBox="0 0 12 12"><path d="M3 1l2 2-1 1.5c.6 1.4 1.6 2.4 3 3L8.5 6.5l2 2-1.5 2C5 10 2 7 1.5 2.5z" fill="var(--gold)"/></svg>
      555-014-2100
    </li>
    <li>
      <svg viewBox="0 0 12 12"><rect x="1" y="2.5" width="10" height="7" fill="none" stroke="var(--gold)" stroke-width="1.2"/><path d="M1 2.5l5 4 5-4" fill="none" stroke="var(--gold)" stroke-width="1.2"/></svg>
      studio@dabneyinteriors.com
    </li>
    <li>
      <svg viewBox="0 0 12 12"><circle cx="6" cy="6" r="5" fill="none" stroke="var(--gold)" stroke-width="1.2"/><path d="M1 6h10M6 1c-2.5 3-2.5 7 0 10M6 1c2.5 3 2.5 7 0 10" fill="none" stroke="var(--gold)" stroke-width="1"/></svg>
      www.dabneyinteriors.com
    </li>
  </ul>

  <p class="address">Your address, city<br>state, ZIP 0000</p>
  <span class="edge-tab"></span>
</section>

<section class="card card--back" aria-label="Business card back">
  <svg class="card-art" viewBox="0 0 540 309">
    <defs>
      <linearGradient id="blushBack" x1="0" y1="0" x2="1" y2="1">
        <stop offset="0" stop-color="#f8d3d4"/>
        <stop offset="1" stop-color="#eeb2a6"/>
      </linearGradient>
    </defs>
    <polygon points="150,0 540,0 540,125" fill="url(#blushBack)" role="img" aria-label="Blush marble texture band"/>
    <polygon points="540,50 540,309 395,309" fill="var(--navy)" role="img" aria-label="Navy textured panel"/>
    <line x1="150" y1="0" x2="540" y2="125" stroke="var(--gold)" stroke-width="2"/>
  </svg>

  <div class="brand-mark"><span class="brand-square"></span>Corinne Dabney Interiors</div>
</section>

</body>
</html>
```